External Window Signage Design – Antiaging Center

I would like to dress our shop windows in order to promote our activities in medical aesthetics, meso-aesthetics, anti-ageing care and classical beauty. In fact, our 350 m² center is located on the first floor of a building where there is a lot of traffic, as well as a bus stop and metro station. And right in front of a twenty-floor building of the Northern Tariff Bureau.
We want to communicate our activities to our customers with photos and text in a storefront window. So that they can what we do and visit our website www.lumivora.be (our site is in French) as well as our social networks, like picturegram, chatterbook,…
We'd like a window signage : Elegant, Modern, New, Pure, Clean
We are located on the corners of a building, where we have 8 windows on one side and 10 windows on the other, the dimensions are :
Windows
• Height: 125 cm
• Width: 130 cm
Small windows
• Height: 134 cm
• Width: 40 cm
I would say let your imagination go free. I will have other projects for the winner.
Don't hesitate to ask me if you need other formats of the logo or color, like white.
Updates

https://www.pixelbazaar-example.com/design/58204917, I'D LIKE TO HAVE A PROJECT LIKE THIS IF POSSIBLE WITH THE LITTLE WINDOW UNDERNEATH AS WELL.

Target Market(s)

People who want to take care of their external appearance, look beautiful and good looking, womens/girls - mens/boys

Requirements
Must have
• Face and silhouette of a woman. Elegant
Serious, Modern, Professional, Feminine,Upmarket
Nice to have
• To put the different treatments that we propose,
Should not have
• We absolutely don't want a classic beauty center signage, which is reviewed many times

```html
<!DOCTYPE html>
<html lang="fr">
<head>
<meta charset="utf-8">
<title>Lumivora Antiaging Center – Window Signage</title>
<link rel="stylesheet" href="https://fonts.googleapis.com/css2?family=Poppins:wght@300;400;500;600;700&display=swap">
<style>
  :root {
    --gold: #b89a5c;
    --ink: #111111;
    --charcoal: #3a3a3c;
    --grey-text: #555557;
    --shadow-grey: #c9c9c9;
    --white: #ffffff;
    --stage: #ececec;
  }
  * { margin: 0; padding: 0; box-sizing: border-box; }
  html, body {
    width: 1133px; height: 1200px; overflow: hidden;
    background: var(--stage);
    font-family: "Poppins", sans-serif;
  }
  .signage {
    position: absolute; left: 8px; top: 63px;
    width: 1596px; height: 1533px;
    transform: scale(0.7); transform-origin: top left;
    background: var(--white);
    overflow: hidden;
  }
  .signage__shapes { position: absolute; inset: 0; width: 1596px; height: 1533px; }
  .portrait {
    position: absolute; inset: 0;
    background: linear-gradient(172deg, #0c0c0c 0%, #1d1d1d 40%, #6f6f6f 66%, #9a9a9a 78%, #3a3a3a 100%);
    clip-path: polygon(1020px 0, 1596px 0, 1596px 1533px, 905px 1533px, 905px 1290px, 990px 1160px, 1010px 760px, 870px 520px, 880px 260px);
  }
  .brand { position: absolute; left: 45px; top: 62px; }
  .brand__name {
    font-weight: 700; font-size: 130px; line-height: 1;
    letter-spacing: -5px; color: var(--charcoal);
  }
  .brand__tagline {
    font-weight: 400; font-size: 38px; color: var(--grey-text);
    padding-left: 150px; line-height: 1.1;
  }
  .section-title {
    position: absolute; left: 45px; top: 334px;
    font-weight: 600; font-size: 70px; line-height: 1.2;
    color: var(--gold); letter-spacing: 1px;
  }
  .treatments { position: absolute; left: 44px; top: 482px; list-style: none; }
  .treatments__item {
    display: flex; align-items: center; height: 75px;
    font-weight: 500; font-size: 62px; color: var(--ink);
  }
  .treatments__tick { width: 38px; height: 38px; margin-right: 21px; flex: none; }
  .contact { position: absolute; left: 44px; top: 1238px; color: var(--white); }
  .contact__call { display: flex; align-items: flex-start; height: 154px; }
  .contact__phone-icon { width: 80px; height: 147px; margin-right: 10px; margin-top: 4px; }
  .contact__label { font-weight: 300; font-size: 68px; line-height: 62px; height: 62px; }
  .contact__number { font-weight: 700; font-size: 126px; line-height: 92px; height: 92px; letter-spacing: -1px; }
  .contact__line {
    display: flex; align-items: center; height: 50px; line-height: 1;
    margin-top: 3px;
    font-weight: 500; font-size: 40px; color: var(--ink);
  }
  .contact__line--web { letter-spacing: 4px; margin-top: 8px; }
  .contact__line svg { width: 36px; height: 36px; margin-right: 12px; flex: none; }
  .social { position: absolute; left: 772px; top: 1456px; display: flex; gap: 10px; }
  .social__dot { width: 42px; height: 42px; border-radius: 50%; background: var(--ink); }
</style>
</head>
<body>
  <div class="signage">
    <svg class="signage__shapes" viewBox="0 0 1596 1533" aria-hidden="true">
      <polygon points="0,345 545,345 490,450 0,450" fill="var(--shadow-grey)"/>
      <polygon points="0,318 535,318 480,436 0,436" fill="var(--ink)"/>
      <path d="M0,1058 C90,1030 170,1032 235,1080 C300,1130 345,1170 420,1165 C500,1160 560,1100 630,1102 C720,1106 760,1215 850,1262 C880,1278 905,1282 930,1282 L930,1533 L0,1533 Z" fill="var(--ink)"/>
      <path d="M0,1072 C90,1046 170,1050 235,1096 C300,1142 345,1178 420,1174 C500,1170 560,1112 630,1114 C720,1118 760,1230 850,1275 C880,1290 905,1294 930,1294 L930,1533 L0,1533 Z" fill="var(--gold)"/>
    </svg>

    <div class="portrait" role="img" aria-label="Black and white portrait of an elegant woman with dark hair, looking down over her shoulder"></div>

    <div class="brand">
      <div class="brand__name">Lumivora</div>
      <div class="brand__tagline">Antiaging Center</div>
    </div>

    <h2 class="section-title">Treatments</h2>

    <ul class="treatments">
      <li class="treatments__item"><svg class="treatments__tick" viewBox="0 0 38 38"><circle cx="19" cy="19" r="19" fill="var(--gold)"/><path d="M11 19.5l5.5 5.5L27 14" fill="none" stroke="#fff" stroke-width="4" stroke-linecap="round" stroke-linejoin="round"/></svg>Antiaging</li>
      <li class="treatments__item"><svg class="treatments__tick" viewBox="0 0 38 38"><circle cx="19" cy="19" r="19" fill="var(--gold)"/><path d="M11 19.5l5.5 5.5L27 14" fill="none" stroke="#fff" stroke-width="4" stroke-linecap="round" stroke-linejoin="round"/></svg>Traitement de peau</li>
      <li class="treatments__item"><svg class="treatments__tick" viewBox="0 0 38 38"><circle cx="19" cy="19" r="19" fill="var(--gold)"/><path d="M11 19.5l5.5 5.5L27 14" fill="none" stroke="#fff" stroke-width="4" stroke-linecap="round" stroke-linejoin="round"/></svg>Amincissement &amp;</li>
      <li class="treatments__item"><svg class="treatments__tick" viewBox="0 0 38 38"><circle cx="19" cy="19" r="19" fill="var(--gold)"/><path d="M11 19.5l5.5 5.5L27 14" fill="none" stroke="#fff" stroke-width="4" stroke-linecap="round" stroke-linejoin="round"/></svg>cellulite</li>
      <li class="treatments__item"><svg class="treatments__tick" viewBox="0 0 38 38"><circle cx="19" cy="19" r="19" fill="var(--gold)"/><path d="M11 19.5l5.5 5.5L27 14" fill="none" stroke="#fff" stroke-width="4" stroke-linecap="round" stroke-linejoin="round"/></svg>Traitement laser</li>
      <li class="treatments__item"><svg class="treatments__tick" viewBox="0 0 38 38"><circle cx="19" cy="19" r="19" fill="var(--gold)"/><path d="M11 19.5l5.5 5.5L27 14" fill="none" stroke="#fff" stroke-width="4" stroke-linecap="round" stroke-linejoin="round"/></svg>Beauté esthétique</li>
      <li class="treatments__item"><svg class="treatments__tick" viewBox="0 0 38 38"><circle cx="19" cy="19" r="19" fill="var(--gold)"/><path d="M11 19.5l5.5 5.5L27 14" fill="none" stroke="#fff" stroke-width="4" stroke-linecap="round" stroke-linejoin="round"/></svg>Traitement divers</li>
    </ul>

    <div class="contact">
      <div class="contact__call">
        <svg class="contact__phone-icon" viewBox="0 0 80 147" aria-hidden="true">
          <rect x="3" y="3" width="74" height="141" rx="9" fill="none" stroke="#fff" stroke-width="6"/>
          <line x1="3" y1="22" x2="77" y2="22" stroke="#fff" stroke-width="4"/>
          <line x1="3" y1="124" x2="77" y2="124" stroke="#fff" stroke-width="4"/>
          <rect x="30" y="130" width="20" height="7" rx="3" fill="#fff"/>
          <line x1="32" y1="12" x2="50" y2="12" stroke="#fff" stroke-width="3" stroke-linecap="round"/>
        </svg>
        <div>
          <div class="contact__label">CALL US ON</div>
          <div class="contact__number">02 418 77 29</div>
        </div>
      </div>
      <div class="contact__line contact__line--web">
        <svg viewBox="0 0 36 36" aria-hidden="true"><g fill="none" stroke="var(--ink)" stroke-width="2.5"><circle cx="18" cy="18" r="15"/><ellipse cx="18" cy="18" rx="7" ry="15"/><line x1="3" y1="18" x2="33" y2="18"/><line x1="6" y1="10" x2="30" y2="10"/><line x1="6" y1="26" x2="30" y2="26"/></g></svg>
        www.lumivora.be
      </div>
      <div class="contact__line">
        <svg viewBox="0 0 36 36" aria-hidden="true"><rect x="2" y="8" width="32" height="22" rx="2" fill="var(--ink)"/><path d="M3 10l15 11 15-11" fill="none" stroke="var(--gold)" stroke-width="2.5"/></svg>
        info@lumivora.be
      </div>
    </div>

    <div class="social" aria-label="chatterbook and picturegram">
      <span class="social__dot"></span>
      <span class="social__dot"></span>
    </div>
  </div>
</body>
</html>
```